Harlow Ridge & Partners Engineers- WEB DESIGN

I am seeking a more professional face to my current website.

www.HRPengineers.com.au

Using same pages and same text, i need the pages to be presented in a more professional manner.

Use Same logo however all other items may be changed to make it look better... Main theme being a navy blue.

Reason: Alot of recent interest. Awaiting designs.

Target Market(s)

Engineers, Students, Public, Local Authorities, Draftsmen, Architects, Builders etc

Requirements
Must have
• Logo as per site,
• Navy Blue Theme,
• Professional feel,
• Images to attract eye and clients attention. (dont use large infrastructure yet more Residential designs, Crack inspections and Residential Construction)

```html
<!DOCTYPE html>
<html lang="en">
<head>
<meta charset="utf-8">
<title>Harlow Ridge &amp; Partners Engineers</title>
<link href="https://fonts.googleapis.com/css2?family=Jost:wght@400;500;600&family=Oswald:wght@700&display=swap" rel="stylesheet">
<style>
  :root {
    --navy: #0b2f8e;
    --navy-deep: #082676;
    --navy-glow: #1a5bb0;
    --card-panel: #e9f1fc;
    --heading-blue: #17479a;
    --body-blue: #1c3f8c;
    --sky: #3b9be6;
    --form-grey: #eef1f1;
    --footer-panel: #eef1f0;
    --white: #ffffff;
  }
  * { margin: 0; padding: 0; box-sizing: border-box; }
  html, body { width: 1200px; height: 1000px; overflow: hidden; }
  body {
    position: relative;
    font-family: "Jost", "Futura", sans-serif;
    background: radial-gradient(ellipse 700px 450px at 600px 560px, var(--navy-glow), var(--navy) 70%, var(--navy-deep));
  }
  .hero {
    position: absolute; left: 0; top: 0; width: 1200px; height: 195px;
    background: linear-gradient(180deg, #c98f52 0%, #b87a3e 45%, #7a4a22 100%);
  }
  .enquiry-form {
    position: absolute; left: 78px; top: -10px; width: 307px; height: 86px;
    background: var(--form-grey); border: 2px solid #cfd6d9; border-radius: 0 0 10px 10px;
  }
  .enquiry-form label {
    position: absolute; left: 22px; top: 10px; font-size: 13px; font-weight: 600; color: #2a2a2a;
  }
  .enquiry-form .field {
    position: absolute; left: 66px; top: 8px; width: 222px; height: 22px;
    background: var(--white); border: 1px solid #c7cdd0;
  }
  .enquiry-form .submit {
    position: absolute; left: 108px; top: 42px; width: 179px; height: 28px;
    border-radius: 14px; background: #1f4fa3; color: var(--white);
    font-size: 14px; font-weight: 500; text-align: center; line-height: 28px; letter-spacing: .3px;
  }
  .service {
    position: absolute; top: 230px; width: 354px; height: 501px;
    border-radius: 10px; overflow: hidden; background: var(--card-panel);
  }
  .service.structural { left: 45px; }
  .service.energy { left: 423px; }
  .service.inspections { left: 801px; }
  .service-image { height: 194px; }
  .structural .service-image { background: linear-gradient(180deg, #6f8fc4 0%, #a9bde0 45%, #7e93b8 100%); }
  .energy .service-image { background: linear-gradient(180deg, #ffffff 0%, #dbe7f7 55%, #eef4fd 100%); }
  .inspections .service-image { background: linear-gradient(120deg, #4d6ea6 0%, #b7c9e6 50%, #7b95c2 100%); }
  .service h2 {
    font-family: "Oswald", "Impact", sans-serif; font-weight: 700;
    font-size: 44px; line-height: 42px; color: var(--heading-blue);
    margin: 18px 0 0 27px; letter-spacing: .2px; text-transform: uppercase;
  }
  .energy h2, .inspections h2 { margin-left: 33px; }
  .inspections h2 { margin-left: 30px; }
  .service p {
    position: absolute; top: 320px; left: 27px; width: 305px;
    font-size: 13.4px; line-height: 19px; color: var(--body-blue);
  }
  .energy p, .inspections p { left: 29px; }
  .read-more {
    position: absolute; left: 0; bottom: 0; width: 100%; height: 49px;
    background: var(--sky); color: var(--white);
    font-size: 15.5px; font-weight: 500; text-align: right; line-height: 46px; padding-right: 22px;
  }
  .footer-links {
    position: absolute; left: 49px; top: 823px; color: var(--white); font-size: 14.5px; font-weight: 500;
  }
  .copyright {
    position: absolute; right: 45px; top: 823px; color: var(--white); font-size: 14.5px; font-weight: 500;
  }
  .affiliations {
    position: absolute; left: 45px; top: 867px; width: 1110px; height: 150px;
    background: var(--footer-panel); border-radius: 10px 10px 0 0;
  }
  .affiliations svg { position: absolute; left: 0; top: 0; }
</style>
</head>
<body>
  <header class="hero" role="img" aria-label="Timber-framed residential building under construction"></header>

  <form class="enquiry-form">
    <label>Email:</label>
    <span class="field"></span>
    <span class="submit">SUBMIT FORM</span>
  </form>

  <article class="service structural">
    <div class="service-image" role="img" aria-label="Two engineers reviewing plans on a steel-frame construction site"></div>
    <h2>Structural<br>Engineering</h2>
    <p>Lorem ipsum dolor sit amet, consectetur adipiscing elit. Aliquam vel mi erat. Nulla facilisi. Etiam aliquet at urna volutpat molestie. Donec venenatis, neque in porttitor blandit, tortor dolor convallis nunc, a sollicitudin metus ipsum non felis. In rhoncus diam arcu, vel semper sapien imperdiet quis.</p>
    <div class="read-more">READ MORE &gt;</div>
  </article>

  <article class="service energy">
    <div class="service-image" role="img" aria-label="Row of house shapes rising in height, graded A to G"></div>
    <h2>Energy<br>Rating</h2>
    <p>Lorem ipsum dolor sit amet, consectetur adipiscing elit. Aliquam vel mi erat. Nulla facilisi. Etiam aliquet at urna volutpat molestie. Donec venenatis, neque in porttitor blandit, tortor dolor convallis nunc, a sollicitudin metus ipsum non felis. In rhoncus diam arcu, vel semper sapien imperdiet quis.</p>
    <div class="read-more">READ MORE &gt;</div>
  </article>

  <article class="service inspections">
    <div class="service-image" role="img" aria-label="Inspector in a hard hat checking a house wall"></div>
    <h2>House<br>Inspections</h2>
    <p>Lorem ipsum dolor sit amet, consectetur adipiscing elit. Aliquam vel mi erat. Nulla facilisi. Etiam aliquet at urna volutpat molestie. Donec venenatis, neque in porttitor blandit, tortor dolor convallis nunc, a sollicitudin metus ipsum non felis. In rhoncus diam arcu, vel semper sapien imperdiet quis.</p>
    <div class="read-more">READ MORE &gt;</div>
  </article>

  <nav class="footer-links">Register Now|Contact Us|</nav>
  <div class="copyright">© 2013. Harlow Ridge &amp; Partners Engineers. All Rights Reserved</div>

  <footer class="affiliations">
    <svg width="1110" height="133" viewBox="0 0 1110 133" aria-label="Industry memberships">
      <circle cx="323" cy="68" r="24" fill="none" stroke="#1f3f8f" stroke-width="3"/>
      <rect x="353" y="50" width="140" height="38" rx="3" fill="#1f3f8f"/>
      <rect x="538" y="33" width="62" height="72" fill="#e3231c"/>
      <rect x="645" y="28" width="56" height="62" rx="8" fill="#2fa23a"/>
      <rect x="750" y="27" width="54" height="78" fill="#2a5fd0"/>
    </svg>
  </footer>
</body>
</html>
```